Packaging / Logo Design for Toddler Potty Liners

We need a packaging and logo design for a new company based in Atlanta called "BrimLeaf". We manufacture innovative, eco-friendly baby / toddler products. Our initial product is a flushable, biodegradable potty liner used for toddler potty training. We are looking for a modern / clean / eco-friendly packaging and logo design for this product. Each package will contain 20 liners. Box dimensions are as follows:

Length = 8.5in
Width = 5in
Height = 1.5in

The box will have a perforated top measuring 6.5 inches (see attached pictures). Liners will be folded inside and individually pulled out through the perforated top (similar to a Softora box). See attached pictures of similar box.

Packaging should appeal to parents as an easy to use, eco-friendly, sanitary solution to potty training. This product is an alternative to the conventional way of cleaning / disinfecting the potty after each use, a process that most parents dread!

The closest competitors are NeatPips (www.neatpips-example.com) and Lumbra (www.lumbra-example.com) - you can reference their websites to get an idea for the product and use. However, their liners are not flushable and that is the biggest differentiator of this product. Their packaging seems conventional and non-inspiring so we would like our design to stand out from theirs.

We would like to see creative, modern cardboard box designs which will make our brand stand out from the competition. We would like to use one of the following color schemes: 1) a modern green color on a white background, 2) a modern green color on plain cardboard background, or 3) white on a modern green background. May use one or two additional complementary colors. See attached modern green image for inspiration. We would like to see clean lines, text and illustrations. We are looking forward to seeing any cool ideas you may have!
Updates

Brief has been updated with our desired color schemes and pictures for inspiration.  Please read updated brief before beginning your design!  Thanks so much!

Industry/Entity Type

Biodegradable

Requirements
Must have
• The front of the package should include the following info:

Logo: BrimLeaf
Product Name: Flushable Potty Chair Liners
Clean and Convenient
Fits All Potty Chairs
Sewer and Septic Safe
Patent Pending
20 Single-Use Flushable Potty Chair Liners

Package should also have space for some simple instructions (preferably with illustrations). This can be placed on one of the sides of the box.
1. Place liner over clean, dry (underline the word dry) potty bowl.
2. After your toddler uses the potty, remove liner (do not tie) and flush.
3. Give your toddler a high five!

Please submit design considering all sides of the box!

```html
<!DOCTYPE html>
<html lang="en">
<head>
<meta charset="utf-8">
<title>BrimLeaf Flushable Potty Chair Liners – Box Panels</title>
<link href="https://fonts.googleapis.com/css2?family=Nunito:wght@400;700;800;900&display=swap" rel="stylesheet">
<style>
  :root{
    --stage:#9a9a9a;
    --stage-light:#c9c9c9;
    --kraft:#d5cab2;
    --green:#2f8a2c;
    --green-dark:#1f6b1f;
    --green-light:#8cc44f;
    --ground:#c4c4c0;
    --ground-dark:#adada9;
    --white:#ffffff;
    --label:#111111;
  }
  *{box-sizing:border-box;margin:0;padding:0}
  html,body{width:1200px;height:900px;overflow:hidden}
  body{
    background:radial-gradient(ellipse at 50% 35%,var(--stage-light),var(--stage));
    font-family:"Nunito",sans-serif;
    position:relative;
  }
  .panel{position:absolute;background:var(--kraft);overflow:hidden;box-shadow:0 6px 18px rgba(0,0,0,.25)}
  .panel-label{position:absolute;font-weight:800;font-size:15px;letter-spacing:.5px;color:var(--label)}

  .landscape{position:absolute;left:0;right:0;background:linear-gradient(180deg,var(--green-light) 0%,var(--green) 45%,var(--green-dark) 100%)}
  .ground{position:absolute;left:0;right:0;bottom:0;background:linear-gradient(180deg,var(--ground),var(--ground-dark))}
  .cloud{position:absolute;background:var(--white);border-radius:20px;height:12px}

  .brand{display:flex;align-items:center;gap:8px;font-family:"Nunito",sans-serif;font-weight:900;color:var(--green);line-height:1;white-space:nowrap}
  .brand-dot{width:20px;height:20px;border-radius:50%;background:var(--green);flex:none}
  .product-title{font-family:"Nunito",sans-serif;font-weight:900;color:var(--green);text-align:center;line-height:1}

  /* FRONT */
  .front{left:190px;top:62px;width:640px;height:376px}
  .front .brand{position:absolute;left:30px;top:70px;font-size:30px}
  .front .product-title{position:absolute;left:212px;top:28px;width:240px;font-size:34px}
  .features{position:absolute;left:236px;top:152px;list-style:none;color:var(--white);font-weight:700;font-size:14px;line-height:1.35}
  .features li::before{content:"★ ";color:var(--green)}
  .eco-badge{position:absolute;right:30px;top:40px;width:120px;text-align:center;color:var(--white);font-weight:800}
  .eco-badge .single{font-size:17px}
  .eco-badge .row{display:flex;align-items:center;justify-content:center;gap:6px;margin-top:4px}
  .eco-badge .mark{width:30px;height:30px;border-radius:50%;background:var(--green)}
  .eco-badge .pct{font-size:26px}
  .eco-badge .bio{font-size:10px;font-weight:700;margin-top:0}
  .front .landscape{top:214px;height:96px}
  .front .ground{height:70px}
  .count{position:absolute;left:0;right:0;top:256px;text-align:center;color:var(--white);font-weight:800;line-height:1}
  .count .num{font-size:24px;display:block}
  .count .unit{font-size:13px}

  /* SIDE 1 – instructions */
  .side-one{left:68px;top:62px;width:112px;height:376px}
  .instructions-title{position:absolute;left:0;right:0;top:44px;text-align:center;font-size:9px;font-weight:800;color:var(--white);letter-spacing:.5px}
  .step{position:absolute;left:10px;width:92px;height:86px;background:var(--white);border-radius:8px;opacity:.92}
  .step-art{position:absolute;inset:6px 6px 26px 6px;border-radius:6px;background:linear-gradient(180deg,#ecece8,#d8d8d2)}
  .step-num{position:absolute;left:-4px;top:28px;width:22px;height:22px;border-radius:50%;background:var(--green);color:var(--white);font-weight:800;font-size:14px;text-align:center;line-height:22px}
  .step-text{position:absolute;left:6px;right:6px;bottom:4px;font-size:7px;line-height:1.15;color:var(--green-dark);font-weight:700;text-align:center}
  .side-one .landscape{top:214px;height:96px}
  .side-one .ground{height:70px}

  /* BACK */
  .back{left:190px;top:490px;width:640px;height:376px}
  .back .brand{position:absolute;left:70px;top:40px;font-size:26px}
  .back .product-title{position:absolute;left:232px;top:28px;width:160px;font-size:20px}
  .back .landscape{top:196px;height:100px}
  .back .ground{height:80px}
  .info-card{position:absolute;left:110px;top:118px;width:380px;height:178px;background:var(--white);border:3px solid var(--green);border-radius:14px;padding:14px 16px;color:var(--green-dark);font-size:9px;line-height:1.45;font-weight:700}
  .info-card p{margin-bottom:10px}
  .contact{font-size:8.5px;line-height:1.5}

  /* SIDE 2 */
  .side-two{left:838px;top:490px;width:112px;height:376px}
  .side-two .landscape{top:196px;height:100px}
  .side-two .ground{height:80px}
  .side-note{position:absolute;left:16px;top:20px;width:80px;height:230px;background:var(--white);border:2px solid var(--green);border-radius:10px}
  .side-note p{position:absolute;left:50%;top:50%;width:200px;transform:translate(-50%,-50%) rotate(90deg);font-size:8px;line-height:1.4;color:var(--green-dark);font-weight:700;text-align:center}
</style>
</head>
<body>

  <span class="panel-label" style="left:68px;top:444px">SIDE 1</span>
  <section class="panel side-one" aria-label="Side panel with instructions">
    <div class="cloud" style="left:10px;top:14px;width:40px"></div>
    <div class="landscape" role="img" aria-label="Rolling green hills with trees"></div>
    <div class="ground"></div>
    <div class="instructions-title">INSTRUCTIONS</div>
    <div class="step" style="top:60px">
      <div class="step-art" role="img" aria-label="Liner placed over potty bowl"></div>
      <span class="step-num">1</span>
      <p class="step-text">Place liner over clean, <u>dry</u> potty bowl</p>
    </div>
    <div class="step" style="top:156px">
      <div class="step-art" role="img" aria-label="Liner lifted out of potty"></div>
      <span class="step-num">2</span>
      <p class="step-text">Remove liner, do not tie, and flush</p>
    </div>
    <div class="step" style="top:252px">
      <div class="step-art" role="img" aria-label="Parent and toddler high five"></div>
      <span class="step-num">3</span>
      <p class="step-text">Give your toddler a high five</p>
    </div>
  </section>

  <span class="panel-label" style="left:470px;top:444px">FRONT</span>
  <section class="panel front" aria-label="Front panel">
    <div class="cloud" style="left:40px;top:22px;width:70px"></div>
    <div class="cloud" style="left:470px;top:150px;width:60px"></div>
    <div class="cloud" style="left:560px;top:196px;width:50px"></div>
    <div class="landscape" role="img" aria-label="Green hills with trees, a butterfly and a dashed flush path"></div>
    <div class="ground" role="img" aria-label="Grey ground with underground pipes"></div>

    <div class="brand"><span class="brand-dot"></span>BrimLeaf</div>
    <h1 class="product-title">Flushable<br>Potty Chair<br>Liners</h1>

    <ul class="features">
      <li>Fits All Potty Chairs</li>
      <li>Sewer and Septic Safe</li>
      <li>Patent Pending</li>
    </ul>

    <div class="eco-badge">
      <div class="single">Single Use &amp;</div>
      <div class="row"><span class="mark"></span><span class="pct">100%</span></div>
      <div class="bio">Biodegradable</div>
    </div>

    <div class="count"><span class="num">20</span><span class="unit">Liners</span></div>
  </section>

  <span class="panel-label" style="left:480px;top:472px">BACK</span>
  <section class="panel back" aria-label="Back panel">
    <div class="cloud" style="left:30px;top:18px;width:60px"></div>
    <div class="cloud" style="left:520px;top:22px;width:70px"></div>
    <div class="landscape" role="img" aria-label="Green hills with trees and a lamp post"></div>
    <div class="ground"></div>

    <div class="brand"><span class="brand-dot"></span>BrimLeaf</div>
    <h2 class="product-title">Flushable<br>Potty Chair<br>Liners</h2>

    <div class="info-card">
      <p>Lorem ipsum dolor sit amet, consectetur adipisicing elit, sed do eiusmod tempor incididunt ut labore et dolore magna aliqua. Ut enim ad minim veniam, quis nostrud exercitation ullamco laboris nisi ut aliquip ex ea commodo consequat. Duis aute irure dolor in reprehenderit in voluptate velit esse cillum dolore eu fugiat nulla pariatur. Excepteur sint occaecat cupidatat non proident, sunt in culpa qui officia deserunt mollit anim id est laborum.</p>
      <div class="contact">
        BrimLeaf Corporation<br>
        12 Meadow Avenue, Atlanta GA<br>
        Tel: 000 555 0142 / Fax: 000 555 0143<br>
        www.brimleaf-example.com
      </div>
    </div>
  </section>

  <span class="panel-label" style="left:958px;top:480px">SIDE 2</span>
  <section class="panel side-two" aria-label="Side panel two">
    <div class="landscape" role="img" aria-label="Green hills continuing from the back panel"></div>
    <div class="ground"></div>
    <div class="side-note">
      <p>Made from plant based fibres. Store in a cool dry place.</p>
    </div>
  </section>

</body>
</html>
```